Wohnungsbaugenossenschaft sucht Webdesign
Zielgruppe
es geht um eine Wohnungsbaugenossenschaft, die Wohnungen an unterschiedlichen Standorten vermietet. Die Webseite soll die WBG präsentieren. Einerseits sollen die Mieter über 'Laufendes' informiert werden, andereseits sollen aktuelle Mietangebote mittels externen Link für potentielle Mieter angezeigt werden.
Aufgabenstellung
Logo, siehe Dateiupload, die Seite muss aber nicht unbedingt 'grün' sein. Diverse Fotos siehe Dateiupload (müssen nicht alle verwendet werden). Texte siehe jetzige Webseite, es können auch LoremIpsum verwendet werden.
Es soll nur die Startseite gelayoutet werden.

```html
<!DOCTYPE html>
<html lang="de">
<head>
<meta charset="utf-8">
<title>WBG Lindenhof – Startseite</title>
<link href="https://fonts.googleapis.com/css2?family=Roboto:wght@400;700&display=swap" rel="stylesheet">
<style>
:root{
  --green:#087a3c;
  --green-dark:#066a33;
  --red:#c8102e;
  --grey-tile:#c9c9c7;
  --grey-line:#d8d8d8;
  --text:#222;
  --white:#fff;
  --footer:#46433f;
}
*{box-sizing:border-box;margin:0;padding:0}
html,body{width:1200px;height:2372px;overflow:hidden}
body{font-family:"Roboto",Arial,sans-serif;color:var(--text);background:var(--white);position:relative}
.site-header{position:absolute;left:0;top:0;width:1200px;height:171px;background:var(--white)}
.brand{position:absolute;left:123px;top:52px;display:flex;align-items:center;gap:14px}
.brand-mark{width:34px;height:34px;background:var(--green)}
.brand-name{font-size:34px;font-weight:700;color:var(--green)}
.quick-link{position:absolute;top:33px;width:118px;height:123px;border:2px solid var(--green);display:flex;flex-direction:column;align-items:center;justify-content:flex-end;padding-bottom:12px;font-size:17px;font-weight:700;color:var(--text)}
.quick-link svg{margin-bottom:10px}
.quick-contact{left:816px}
.quick-emergency{left:949px}
.main-nav{position:absolute;left:0;top:171px;width:1200px;height:67px;background:var(--green)}
.main-nav a{position:absolute;top:26px;color:var(--white);font-size:15px;font-weight:700;text-decoration:none}
.main-nav a.active::after{content:"";position:absolute;left:0;right:0;bottom:-8px;height:2px;background:var(--white)}
.hero{position:absolute;left:0;top:238px;width:1200px;height:540px;background:linear-gradient(100deg,#6f6a63 0%,#a69c90 30%,#d8d3cc 55%,#e9e6e1 75%,#bdb6ac 100%)}
.hero-title{position:absolute;left:123px;top:222px;font-size:41px;font-weight:700;line-height:1.18;color:var(--white)}
.tiles{position:absolute;left:123px;top:880px;width:944px;height:253px;display:flex}
.tile{position:relative;width:315px;height:253px;overflow:hidden}
.tile-news{background:var(--grey-tile);width:314px}
.tile-news p{font-size:13px;line-height:1.45;color:#333;padding:0 14px;margin-top:12px}
.tile-offers{background:linear-gradient(180deg,#b9c4cf 0%,#8f9499 35%,#d7cfc4 60%,#7d8a6a 100%)}
.tile-emergency{background:var(--red)}
.drop-icon{position:absolute;left:112px;top:48px}
.tile-label{position:absolute;left:0;right:0;bottom:22px;text-align:center;font-size:26px;font-weight:700;color:var(--white)}
.tile-corner{position:absolute;right:0;bottom:0;width:56px;height:56px}
.about{position:absolute;left:0;top:1223px;width:1200px;height:445px;background:var(--green);color:var(--white);text-align:center}
.about h2{margin-top:68px;font-size:23px;font-weight:700}
.about p{width:960px;margin:48px auto 0;font-size:16px;line-height:1.62}
.btn-more{position:absolute;left:476px;top:304px;width:227px;height:54px;background:var(--white);color:var(--text);font-size:17px;font-weight:700;display:flex;align-items:center;justify-content:center}
.contact{position:absolute;left:0;top:1668px;width:1200px;height:604px}
.contact h2{position:absolute;left:0;width:1200px;top:64px;text-align:center;font-size:25px;font-weight:700}
.address{position:absolute;left:123px;top:200px;font-size:17px;line-height:24.5px;font-style:normal}
.form{position:absolute;left:568px;top:153px;width:494px}
.field{position:absolute;border:1px solid var(--grey-line);background:var(--white);font-size:15px;color:#aaa;padding:8px 12px}
.field-select{left:0;top:0;width:248px;height:36px;padding-top:6px}
.field-select svg{position:absolute;right:26px;top:10px}
.f-first{left:0;top:36px;width:240px;height:48px}
.f-last{left:250px;top:36px;width:244px;height:48px}
.f-mail{left:0;top:94px;width:494px;height:48px}
.f-subject{left:0;top:152px;width:494px;height:48px}
.f-message{left:0;top:207px;width:494px;height:131px}
.btn-send{position:absolute;left:0;top:356px;width:115px;height:41px;background:var(--green);color:var(--white);font-size:16px;font-weight:700;display:flex;align-items:center;justify-content:center}
.site-footer{position:absolute;left:0;top:2272px;width:1200px;height:100px;background:var(--footer);color:var(--white);font-size:17px}
.site-footer span{position:absolute;top:40px}
</style>
</head>
<body>
<header class="site-header">
  <div class="brand"><span class="brand-mark"></span><span class="brand-name">WBG Lindenhof</span></div>
  <div class="quick-link quick-contact">
    <svg width="46" height="50" viewBox="0 0 46 50"><path d="M3 3h40v32H18L8 46V35H3z" fill="none" stroke="#222" stroke-width="3" stroke-linejoin="round"/></svg>
    Kontakt
  </div>
  <div class="quick-link quick-emergency">
    <svg width="40" height="54" viewBox="0 0 40 54"><path d="M20 3C26 16 37 26 37 36a17 17 0 0 1-34 0C3 26 14 16 20 3z" fill="none" stroke="#222" stroke-width="3"/></svg>
    Notdienst
  </div>
</header>

<nav class="main-nav">
  <a class="active" style="left:258px">Startseite</a>
  <a style="left:407px">Neuigkeiten</a>
  <a style="left:547px">Objektstandorte</a>
  <a style="left:766px">Die Genossenschaft</a>
</nav>

<section class="hero" role="img" aria-label="Foto: junges Paar sitzt lachend im hellen Wohnzimmer">
  <h1 class="hero-title">Wir vermieten Wohnungen<br>an unterschiedlichen<br>Standorten.</h1>
</section>

<section class="tiles">
  <div class="tile tile-news">
    <p>Abgeschieden wohnen sie in Buchstabhausen an der Küste des Semantik, eines großen Sprach-ozeans.</p>
    <p>Abgeschieden wohnen sie in Buchstabhausen an der Küste des Semantik, eines großen Sprach-ozeans.</p>
    <div class="tile-label">Neuigkeiten</div>
    <svg class="tile-corner" viewBox="0 0 56 56"><path d="M56 0V56H0z" fill="#087a3c"/><path d="M38 26v22M27 37h22" stroke="#fff" stroke-width="4"/></svg>
  </div>
  <div class="tile tile-offers" role="img" aria-label="Foto: Mehrfamilienhaus mit Schieferdach">
    <div class="tile-label">Mietangebote</div>
    <svg class="tile-corner" viewBox="0 0 56 56"><path d="M56 0V56H0z" fill="#087a3c"/><path d="M38 26v22M27 37h22" stroke="#fff" stroke-width="4"/></svg>
  </div>
  <div class="tile tile-emergency">
    <svg class="drop-icon" width="90" height="120" viewBox="0 0 90 120"><path d="M45 6C58 36 84 56 84 80a39 39 0 0 1-78 0C6 56 32 36 45 6z" fill="none" stroke="#e9d3d6" stroke-width="5"/></svg>
    <div class="tile-label">Notdienst</div>
    <svg class="tile-corner" viewBox="0 0 56 56"><path d="M56 0V56H0z" fill="#087a3c"/><path d="M38 26v22M27 37h22" stroke="#fff" stroke-width="4"/></svg>
  </div>
</section>

<section class="about">
  <h2>Die Genossenschaft</h2>
  <p>Wir sind seit 1926 eine eingetragene Genossenschaft und verwalten zur Zeit ca. 456 Wohneinheiten. Neben Mehrfamilienhäusern verwalten wir auch Ein- und Zweifamilienhäuser. Alle Wohnungsstandorte sind rund um das malerische Talstadt gelegen. Die ganze Region gehört zum wunderschönen Bergland. Lassen auch Sie sich von dieser schönen Wohngegend verzaubern.</p>
  <div class="btn-more">mehr</div>
</section>

<section class="contact">
  <h2>Kontakt</h2>
  <address class="address">
    Wohnungsbaugenossenschaft - Lindenhof - eG<br>
    Talstadt<br>
    Birkenweg 14<br>
    01234 Talstadt<br><br>
    E-Mail:&nbsp; info@wbg-lindenhof-talstadt.de<br>
    Telefon: (01234) 55501<br>
    Telefon: (01234) 55502<br>
    Telefax: (01234) 55503
  </address>
  <div class="form">
    <div class="field field-select">Anrede
      <svg width="30" height="16" viewBox="0 0 30 16"><path d="M0 0h30L15 16z" fill="#ddd"/></svg>
    </div>
    <div class="field f-first">Vorname</div>
    <div class="field f-last">Name</div>
    <div class="field f-mail">E-Mail</div>
    <div class="field f-subject">Betreff</div>
    <div class="field f-message">Nachricht</div>
    <div class="btn-send">senden</div>
  </div>
</section>

<footer class="site-footer">
  <span style="left:110px">© Wohnungsbaugenossenschaft - Lindenhof - eG</span>
  <span style="left:788px">Impressum</span>
  <span style="left:944px">Datenschutz</span>
</footer>
</body>
</html>
```